Vintage Carnival Themed, Fresh Food Mashup

I'm looking for product posters that are a mashup of vintage carnival advertising and fresh squeezed orange juice. Must be something that looks cool but also gets your tastebuds going. The initial product is fresh squeezed orange juice smoothies but many more products and advertising items needed.

Industry/Entity Type

Advertising

```html
<!DOCTYPE html>
<html lang="en">
<head>
<meta charset="utf-8">
<title>Don't You Feel Thirsty? Just Squeeze and Feel Fresh</title>
<link rel="stylesheet" href="https://fonts.googleapis.com/css2?family=Rye&family=Sancreek&family=Alfa+Slab+One&display=swap">
<style>
  :root {
    --parchment: #d8b17b;
    --parchment-light: #e6c593;
    --parchment-dark: #c49a62;
    --navy: #37404f;
    --red: #e2202a;
    --orange: #f39a1d;
    --juice: #f8c62a;
    --ribbon: #a7824d;
    --ribbon-dark: #7d6038;
    --cream: #fbe7c8;
    --white: #ffffff;
  }
  html, body {
    margin: 0;
    padding: 0;
    width: 848px;
    height: 1200px;
    overflow: hidden;
    background: var(--parchment);
  }
  .poster {
    position: relative;
    width: 848px;
    height: 1200px;
    overflow: hidden;
    background: radial-gradient(ellipse at 50% 45%, var(--parchment-light) 0%, var(--parchment) 55%, var(--parchment-dark) 100%);
  }
  .poster-art {
    position: absolute;
    inset: 0;
  }
  .headline-lead {
    position: absolute;
    left: 132px;
    width: 584px;
    top: 250px;
    margin: 0;
    text-align: center;
    font-family: "Rye", serif;
    font-weight: 400;
    font-size: 50px;
    letter-spacing: 6px;
    color: var(--red);
    text-shadow: 2px 3px 3px rgba(80, 40, 10, .35);
    white-space: nowrap;
  }
  .headline-main {
    position: absolute;
    left: 120px;
    width: 608px;
    top: 322px;
    margin: 0;
    text-align: center;
    font-family: "Sancreek", serif;
    font-weight: 400;
    font-size: 150px;
    line-height: 1;
    letter-spacing: 2px;
    color: var(--navy);
    white-space: nowrap;
  }
  .juice-splash {
    position: absolute;
    left: 236px;
    top: 380px;
    width: 340px;
    height: 350px;
    border-radius: 48% 52% 46% 54% / 55% 50% 50% 45%;
    background: radial-gradient(ellipse at 50% 70%, var(--orange) 0%, var(--juice) 45%, rgba(248, 198, 42, .0) 72%);
  }
  .banner-text {
    position: absolute;
    left: 148px;
    top: 734px;
    width: 536px;
    height: 110px;
    display: flex;
    align-items: center;
    justify-content: center;
    gap: 14px;
    white-space: nowrap;
  }
  .banner-just {
    font-family: "Rye", serif;
    font-size: 44px;
    color: var(--cream);
    -webkit-text-stroke: 1.5px var(--navy);
    letter-spacing: 2px;
  }
  .banner-squeeze {
    font-family: "Rye", serif;
    font-size: 66px;
    color: var(--orange);
    -webkit-text-stroke: 1px var(--red);
    letter-spacing: 1px;
  }
  .banner-star {
    color: var(--orange);
    font-family: "Alfa Slab One", serif;
    font-size: 26px;
  }
  .tagline-word {
    position: absolute;
    top: 870px;
    margin: 0;
    font-family: "Alfa Slab One", serif;
    font-size: 27px;
    color: var(--white);
    letter-spacing: 1px;
  }
  .tagline-and { left: 258px; }
  .tagline-feel { left: 534px; }
  .tagline-fresh {
    position: absolute;
    left: 280px;
    width: 280px;
    top: 918px;
    margin: 0;
    text-align: center;
    font-family: "Rye", serif;
    font-size: 58px;
    color: var(--white);
    -webkit-text-stroke: 2px var(--navy);
    letter-spacing: 2px;
    white-space: nowrap;
  }
</style>
</head>
<body>
<main class="poster">
  <svg class="poster-art" width="848" height="1200" viewBox="0 0 848 1200" aria-hidden="true">
    <defs>
      <symbol id="star-shape" viewBox="-100 -100 200 200">
        <polygon points="0,-100 23.5,-32.4 95.1,-30.9 38,12.4 58.8,80.9 0,40 -58.8,80.9 -38,12.4 -95.1,-30.9 -23.5,-32.4"/>
      </symbol>
      <path id="frame-outline" d="M424 128 L560 128 C580 128 585 150 600 152 C650 158 700 150 730 178 C760 205 740 240 770 262 C800 285 800 330 780 370 C760 420 770 470 790 520 C810 600 770 660 770 700 C770 760 800 800 780 860 C760 920 770 980 740 1020 C700 1060 620 1050 560 1060 C500 1070 470 1090 424 1092 C378 1090 348 1070 288 1060 C228 1050 148 1060 108 1020 C78 980 88 920 68 860 C48 800 78 760 78 700 C78 660 38 600 58 520 C78 470 88 420 68 370 C48 330 48 285 78 262 C108 240 88 205 118 178 C148 150 198 158 248 152 C263 150 268 128 288 128 Z"/>
      <clipPath id="frame-clip">
        <use href="#frame-outline" transform="translate(424 610) scale(.93 .94) translate(-424 -610)"/>
      </clipPath>
      <pattern id="star-row" x="132" y="232" width="32" height="22" patternUnits="userSpaceOnUse">
        <use href="#star-shape" x="5" y="1" width="22" height="22" fill="var(--red)"/>
      </pattern>
    </defs>

    <g class="corner-marks" fill="var(--navy)">
      <polygon points="20,24 128,24 20,140"/>
      <polygon points="828,24 720,24 828,140"/>
      <polygon points="20,1176 128,1176 20,1060"/>
      <polygon points="828,1176 720,1176 828,1060"/>
    </g>
    <g class="corner-stars" fill="var(--white)">
      <use href="#star-shape" x="38" y="46" width="30" height="30"/>
      <use href="#star-shape" x="780" y="46" width="30" height="30"/>
      <use href="#star-shape" x="38" y="1124" width="30" height="30"/>
      <use href="#star-shape" x="780" y="1124" width="30" height="30"/>
    </g>

    <g class="sunburst" clip-path="url(#frame-clip)">
      <g clip-path="inset(0)">
        <rect x="0" y="610" width="848" height="600" fill="none"/>
      </g>
      <svg x="0" y="610" width="848" height="600" viewBox="0 610 848 600" overflow="hidden">
        <g fill="var(--red)" stroke="var(--white)" stroke-width="3">
          <polygon points="408,664 999,560 1006,716"/>
          <polygon points="408,664 972,869 899,1008"/>
          <polygon points="408,664 794,1124 662,1208"/>
          <polygon points="408,664 512,1255 304,1255"/>
          <polygon points="408,664 154,1208 22,1124"/>
          <polygon points="408,664 -83,1008 -156,869"/>
          <polygon points="408,664 -190,716 -183,560"/>
        </g>
        <path d="M60 1000 C150 1060 300 1050 424 1080 C548 1050 698 1060 788 1000 L800 1120 L48 1120 Z" fill="var(--red)"/>
      </svg>
    </g>

    <g class="frame" fill="none" stroke="var(--navy)">
      <use href="#frame-outline" stroke-width="18"/>
      <use href="#frame-outline" stroke-width="5" transform="translate(424 610) scale(.93 .94) translate(-424 -610)"/>
    </g>

    <rect class="star-row" x="132" y="232" width="584" height="22" fill="url(#star-row)"/>
    <rect class="headline-rule" x="132" y="328" width="584" height="3" fill="var(--red)"/>

    <g class="ribbon">
      <polygon points="8,860 60,822 40,780 160,780 160,860" fill="var(--ribbon)"/>
      <polygon points="840,860 788,822 808,780 688,780 688,860" fill="var(--ribbon)"/>
      <polygon points="160,860 120,860 160,844" fill="var(--ribbon-dark)"/>
      <polygon points="688,860 728,860 688,844" fill="var(--ribbon-dark)"/>
    </g>
    <rect class="banner-plate" x="148" y="734" width="536" height="110" rx="8" fill="var(--cream)" stroke="var(--navy)" stroke-width="5"/>

    <ellipse class="fresh-oval" cx="420" cy="952" rx="142" ry="38" fill="var(--white)" stroke="var(--navy)" stroke-width="4"/>

    <g class="side-stars" fill="var(--white)" stroke="var(--navy)" stroke-width="6">
      <use href="#star-shape" x="28" y="868" width="200" height="200"/>
      <use href="#star-shape" x="604" y="868" width="200" height="200"/>
    </g>
  </svg>

  <h2 class="headline-lead">DON’T YOU FEEL</h2>
  <h1 class="headline-main">THIRSTY?</h1>

  <div class="juice-splash" role="img" aria-label="Half an orange bursting with a splash of fresh orange juice"></div>

  <div class="banner-text">
    <span class="banner-just">JUST</span>
    <span class="banner-star">★</span>
    <span class="banner-squeeze">SQUEEZE</span>
    <span class="banner-star">★</span>
  </div>

  <p class="tagline-word tagline-and">AND</p>
  <p class="tagline-word tagline-feel">FEEL</p>
  <p class="tagline-fresh">FRESH</p>
</main>
</body>
</html>
```